Plastic Surgeon Needs a business card desing

I need a plastic surgeon business card, Im young , innovative , not afraid of thinking out of the box, What I dont like is human figures or scalpes as designing the card, because I think they are old fashion, I think my name is my strongest card, so I try to find the desing to be something elegant , simple , slick , stylish , radiant with carimsa!

Target Market(s)

PLastics Surgery Patients and doctors to have my data

Industry/Entity Type

Plastic

Contact Information for Business Card

phone numbers need to be legible , right now i have grey scales so they a not to legible

Font styles to use
Serif
Sans Serif

Requirements
Must have
• Personality, and it has to look like a doctor card, not a buisness man card, that is why i think it should be clean , clear , and legible
Nice to have
• Stylilsh, not to heavy card, in means of colors and logos, i think it should give a sensation of health
• Im not sure to have the logo of the hospital i work
Should not have
• human figures
• Hands
• Surgeons

```html
<!DOCTYPE html>
<html lang="es">
<head>
<meta charset="utf-8">
<title>Dr. Marco Velasco — Tarjeta</title>
<link rel="stylesheet" href="https://fonts.googleapis.com/css2?family=Bebas+Neue&family=Arimo:wght@400&display=swap">
<style>
  :root {
    --backdrop: #1a6a72;
    --card-white: #ffffff;
    --brand-blue: #3f7fc6;
    --band-black: #161616;
    --band-text: #ffffff;
  }
  * { margin: 0; padding: 0; box-sizing: border-box; }
  html, body {
    width: 1200px;
    height: 710px;
    overflow: hidden;
    background: var(--backdrop);
  }
  .card {
    position: absolute;
    left: 180px;
    top: 115px;
    width: 840px;
    height: 480px;
    background: var(--card-white);
    overflow: hidden;
  }
  .contact {
    position: absolute;
    right: 60px;
    top: 50px;
    text-align: right;
    font-family: "Arimo", Arial, sans-serif;
    font-size: 19px;
    line-height: 30px;
    color: var(--brand-blue);
    list-style: none;
  }
  .identity {
    position: absolute;
    left: 60px;
    top: 196px;
    display: flex;
    align-items: center;
    gap: 22px;
  }
  .identity-mark {
    width: 58px;
    height: 58px;
    border-radius: 50%;
    background: var(--brand-blue);
    flex: none;
  }
  .identity-text {
    font-family: "Bebas Neue", "Arial Narrow", sans-serif;
    color: var(--brand-blue);
  }
  .doctor-name {
    font-size: 74px;
    line-height: 0.95;
    font-weight: 400;
    letter-spacing: 1px;
  }
  .specialty {
    font-size: 30px;
    line-height: 1;
    text-align: right;
    letter-spacing: 1px;
  }
  .address-band {
    position: absolute;
    left: 0;
    bottom: 0;
    width: 100%;
    height: 128px;
    background: var(--band-black);
  }
  .address {
    position: absolute;
    left: 60px;
    top: 34px;
    font-family: "Arimo", Arial, sans-serif;
    font-size: 21px;
    color: var(--band-text);
    white-space: nowrap;
  }
  .band-rule {
    position: absolute;
    left: 0;
    bottom: 26px;
    width: 100%;
    height: 5px;
    background: var(--card-white);
  }
</style>
</head>
<body>
  <article class="card">
    <ul class="contact">
      <li>Email : marco@drvelasco.com</li>
      <li>Web : www.drvelasco.com</li>
      <li>Tel : 021 (33) 5550 1234</li>
      <li>Cel : 33 5550 9876</li>
    </ul>

    <div class="identity">
      <span class="identity-mark"></span>
      <div class="identity-text">
        <h1 class="doctor-name">Dr. Marco Velasco</h1>
        <p class="specialty">Cirugia Plastica</p>
      </div>
    </div>

    <footer class="address-band">
      <p class="address">Calle Olmos 1580 Int 214 Torre Medica Horizonte Guadalajara, Jal Mexico</p>
      <div class="band-rule"></div>
    </footer>
  </article>
</body>
</html>
```